Stationary/Web Page
Project: Business Cards
Business Cards
Professional
Joel Varrick
President
4817 W. Pelham Ridge Dunmore Rd. Baytown, TX 77409
JoelVarrick_OTW@mailbrook.com

```html
<!DOCTYPE html>
<html lang="en">
<head>
<meta charset="utf-8">
<title>Oakfield Tradeworks Stationery</title>
<link href="https://fonts.googleapis.com/css2?family=Arimo:wght@400;700&display=swap" rel="stylesheet">
<style>
:root{
  --bg:#e4e4e4;
  --paper:#ffffff;
  --red:#c8141c;
  --red-dark:#5e0608;
  --red-deep:#8a0c10;
  --ink:#3a3a3a;
  --muted:#8a8a8a;
  --faint:#ececec;
  --line:#c9c9c9;
}
*{margin:0;padding:0;box-sizing:border-box}
html,body{width:1200px;height:679px;overflow:hidden}
body{background:var(--bg);font-family:"Arimo",Arial,sans-serif;color:var(--ink);position:relative}
.label{position:absolute;left:53px;width:187px;text-align:center;font-size:7px;font-weight:700;color:var(--ink)}
.card{position:absolute;left:53px;width:187px;height:86px;overflow:hidden;box-shadow:0 2px 5px rgba(0,0,0,.28)}
.card.rounded{border-radius:9px}
.card-front{background:linear-gradient(180deg,#ffffff,#ececec)}
.card-front .swoosh{position:absolute;left:0;top:0;width:100%;height:100%}
.card-front .brand{position:absolute;left:9px;top:9px}
.card-front .person{position:absolute;right:14px;top:36px;text-align:right;font-size:6.5px;line-height:1.3}
.person .name{font-weight:700;font-size:8px;color:var(--ink)}
.person .title{color:var(--muted)}
.card-front .contact{position:absolute;right:14px;top:58px;text-align:right;font-size:4.2px;line-height:1.35;color:var(--ink)}
.card-back{background:radial-gradient(ellipse at 50% 45%,var(--red) 0%,var(--red-deep) 55%,var(--red-dark) 100%)}
.card-back .brand{position:absolute;left:50%;top:50%;transform:translate(-50%,-50%);flex-direction:column;gap:3px;text-align:center}
.brand{display:flex;align-items:center;gap:4px}
.brand .dot{border-radius:50%;background:var(--red);flex:none}
.brand .word{font-weight:700;color:var(--red);line-height:1.1;letter-spacing:.2px;white-space:nowrap}
.brand.light .dot{background:#ffffff}
.brand.light .word{color:#ffffff}
.card .brand .dot{width:11px;height:11px}
.card .brand .word{font-size:6px}
.card-back .brand .dot{width:22px;height:22px}
.card-back .brand .word{font-size:7px}
.page{position:absolute;top:29px;width:430px;height:624px;background:var(--paper);box-shadow:0 2px 8px rgba(0,0,0,.25);overflow:hidden}
.letterhead{left:264px}
.fax-sheet{left:722px}
.page .brand{position:absolute;left:20px;top:20px}
.page .brand .dot{width:18px;height:18px}
.page .brand .word{font-size:10px}
.page .address{position:absolute;right:22px;top:18px;text-align:right;font-size:4.4px;line-height:1.4;color:var(--ink)}
.page .emblem{position:absolute;left:85px;top:145px;width:260px;height:260px;border-radius:50%;background:var(--faint)}
.page .wave{position:absolute;left:0;bottom:0;width:100%;height:48px}
.fax-title{position:absolute;left:20px;top:100px;font-size:30px;font-weight:700;color:var(--red);letter-spacing:1px}
.fax-table{position:absolute;left:20px;top:142px;width:390px;display:grid;grid-template-columns:1fr 1fr;column-gap:18px;row-gap:5px}
.field{display:flex;align-items:center;gap:4px}
.field .tag{width:44px;height:11px;background:var(--red);color:#fff;font-size:5.5px;font-weight:700;padding-left:4px;line-height:11px}
.field .fill{flex:1;border-bottom:1px dotted var(--line);height:8px}
.checks{position:absolute;left:40px;top:226px;display:flex;gap:22px;font-size:5px;color:var(--ink)}
.checks span{display:flex;align-items:center;gap:4px}
.checks i{display:inline-block;width:6px;height:6px;border:1px solid var(--muted)}
.comments{position:absolute;left:20px;top:246px;font-size:5.5px;font-weight:700}
</style>
</head>
<body>

<div class="label" style="top:79px">Business Card Rounded</div>

<div class="card rounded card-front" style="top:91px">
  <svg class="swoosh" viewBox="0 0 187 86" preserveAspectRatio="none" aria-hidden="true">
    <path d="M0 0 H160 C115 8 68 26 42 86 H0 Z" fill="var(--red)"/>
    <path d="M0 0 H150 C105 6 58 22 30 86 H0 Z" fill="var(--red-dark)"/>
  </svg>
  <div class="brand light"><span class="dot"></span><span class="word">OAKFIELD<br>TRADEWORKS LLC</span></div>
  <div class="person"><div class="name">Joel Varrick</div><div class="title">President</div></div>
  <div class="contact">4817 W. Pelham Ridge Dunmore Rd.<br>Baytown, TX 77409<br>Phone 281.555.0142<br>JoelVarrick_OTW@mailbrook.com</div>
</div>

<div class="card rounded card-back" style="top:194px">
  <div class="brand light"><span class="dot"></span><span class="word">OAKFIELD<br>TRADEWORKS LLC</span></div>
</div>

<div class="label" style="top:365px">Business Card Standard</div>

<div class="card card-front" style="top:384px">
  <svg class="swoosh" viewBox="0 0 187 86" preserveAspectRatio="none" aria-hidden="true">
    <path d="M0 0 H160 C115 8 68 26 42 86 H0 Z" fill="var(--red)"/>
    <path d="M0 0 H150 C105 6 58 22 30 86 H0 Z" fill="var(--red-dark)"/>
  </svg>
  <div class="brand light"><span class="dot"></span><span class="word">OAKFIELD<br>TRADEWORKS LLC</span></div>
  <div class="person"><div class="name">Joel Varrick</div><div class="title">President</div></div>
  <div class="contact">4817 W. Pelham Ridge Dunmore Rd.<br>Baytown, TX 77409<br>Phone 281.555.0142<br>JoelVarrick_OTW@mailbrook.com</div>
</div>

<div class="card card-back" style="top:487px">
  <div class="brand light"><span class="dot"></span><span class="word">OAKFIELD<br>TRADEWORKS LLC</span></div>
</div>

<section class="page letterhead">
  <div class="brand"><span class="dot"></span><span class="word">OAKFIELD<br>TRADEWORKS LLC</span></div>
  <div class="address">4817 W. Pelham Ridge Dunmore Rd.<br>Baytown, TX 77409<br>Phone 281.555.0142<br>Fax 281.555.0143</div>
  <div class="emblem"></div>
  <svg class="wave" viewBox="0 0 430 48" preserveAspectRatio="none" aria-hidden="true">
    <defs><linearGradient id="waveA" x1="0" x2="1"><stop offset="0" stop-color="var(--red-dark)"/><stop offset=".5" stop-color="var(--red)"/><stop offset="1" stop-color="var(--red-dark)"/></linearGradient></defs>
    <path d="M0 22 C120 2 300 2 430 18 V48 H0 Z" fill="url(#waveA)"/>
  </svg>
</section>

<section class="page fax-sheet">
  <div class="brand"><span class="dot"></span><span class="word">OAKFIELD<br>TRADEWORKS LLC</span></div>
  <div class="address">4817 W. Pelham Ridge Dunmore Rd.<br>Baytown, TX 77409<br>Phone 281.555.0142<br>Fax 281.555.0143</div>
  <div class="emblem"></div>
  <div class="fax-title">FAX</div>
  <div class="fax-table">
    <div class="field"><span class="tag">To</span><span class="fill"></span></div>
    <div class="field"><span class="tag">From</span><span class="fill"></span></div>
    <div class="field"><span class="tag">Fax</span><span class="fill"></span></div>
    <div class="field"><span class="tag">Pages</span><span class="fill"></span></div>
    <div class="field"><span class="tag">Phone</span><span class="fill"></span></div>
    <div class="field"><span class="tag">Date</span><span class="fill"></span></div>
    <div class="field"><span class="tag">Re</span><span class="fill"></span></div>
    <div class="field"><span class="tag">CC</span><span class="fill"></span></div>
  </div>
  <div class="checks">
    <span><i></i>Urgent</span><span><i></i>For Review</span><span><i></i>Please Comment</span><span><i></i>Please Reply</span><span><i></i>Please Recycle</span>
  </div>
  <div class="comments">Comments :</div>
  <svg class="wave" viewBox="0 0 430 48" preserveAspectRatio="none" aria-hidden="true">
    <defs><linearGradient id="waveB" x1="0" x2="1"><stop offset="0" stop-color="var(--red-dark)"/><stop offset=".5" stop-color="var(--red)"/><stop offset="1" stop-color="var(--red-dark)"/></linearGradient></defs>
    <path d="M0 22 C120 2 300 2 430 18 V48 H0 Z" fill="url(#waveB)"/>
  </svg>
</section>

</body>
</html>
```